VornaDerm/The experts in permanent hairremoval

Our Brand is VornaDerm and we are specialized on permantent hair removal for the body for men and woman. VornaDerm is working as a Franchise chain.
The brand should be positioned as lifestyle brand but with a medical background. People should trust in us. We take care about their body. This need to be communicated 100%.
Our system is inexpensive but we don't want to show that we are cheap. So we want to communicate that permanent hair removal is a real lifestyle product but affordable.
We already created a logo that you can see the style and colour we prefer.

Target Market(s)

Europe beginning (especially german spoken markets), Middle East, Africa

Industry/Entity Type

Hair Removal

Number of Pages Required

5+ page

Font styles to use
Serif
Other font styles liked:
• Trajan Pro

Requirements
Nice to have
• We are very open for new ideas

```html
<!DOCTYPE html>
<html lang="en">
<head>
<meta charset="utf-8">
<title>VornaDerm – The experts in permanent hair removal</title>
<link rel="stylesheet" href="https://fonts.googleapis.com/css2?family=Cinzel:wght@400;600;700&display=swap">
<style>
  :root {
    --bg: #f6f6f6;
    --ink: #333333;
    --ink-soft: #555555;
    --sky: #5cb5e5;
    --sky-deep: #3a9ad9;
    --band: #60b6e4;
    --white: #ffffff;
    --icon-line: #9a9a9a;
  }
  * { margin: 0; padding: 0; box-sizing: border-box; }
  html, body { width: 1200px; height: 675px; overflow: hidden; }
  body {
    position: relative;
    font-family: "Cinzel", serif;
    color: var(--ink);
    background: radial-gradient(ellipse at 35% 40%, #ffffff 0%, var(--bg) 55%, #ececec 100%);
  }
  .brand { position: absolute; left: 174px; top: 44px; display: flex; align-items: center; gap: 10px; }
  .brand-dot { width: 34px; height: 34px; border-radius: 50%; background: var(--sky); }
  .brand-name { font-size: 34px; font-weight: 400; color: var(--ink-soft); line-height: 1; letter-spacing: 0.5px; }
  .brand-tagline { position: absolute; left: 218px; top: 90px; font-size: 6.5px; color: var(--ink-soft); letter-spacing: 0.3px; }
  .brand-rule { position: absolute; left: 218px; top: 44px; width: 1px; height: 62px; background: #dcdcdc; }

  .enquire { position: absolute; left: 514px; top: 36px; display: flex; align-items: center; gap: 8px; font-size: 11px; color: var(--ink-soft); }
  .enquire b { color: var(--ink); font-weight: 700; }
  .social { position: absolute; left: 759px; top: 34px; display: flex; gap: 7px; }
  .social span { width: 18px; height: 18px; border: 1px solid var(--icon-line); border-radius: 50%; }
  .book-btn {
    position: absolute; left: 858px; top: 26px; width: 177px; height: 32px;
    border-radius: 16px; background: var(--sky); color: var(--white);
    font-size: 11.5px; display: flex; align-items: center; justify-content: center; letter-spacing: 0.3px;
  }
  .main-nav { position: absolute; top: 80px; left: 531px; display: flex; gap: 0; font-size: 13.5px; }
  .main-nav a { color: var(--ink); text-decoration: none; margin-right: 28px; }
  .main-nav a:last-child { margin-right: 0; }

  .headline {
    position: absolute; left: 174px; top: 180px;
    font-size: 64px; font-weight: 700; line-height: 84px; color: var(--ink);
    text-shadow: 0 2px 3px rgba(0,0,0,0.18);
  }
  .why { position: absolute; left: 174px; top: 464px; display: flex; align-items: center; gap: 9px; font-size: 16px; color: var(--sky-deep); }
  .why-dot { width: 14px; height: 14px; border-radius: 50%; background: var(--sky); }
  .why-links { position: absolute; left: 174px; top: 494px; font-size: 12px; color: var(--sky-deep); }
  .why-links span { color: var(--ink-soft); }

  .hero-photo {
    position: absolute; left: 770px; top: 128px; width: 430px; height: 484px;
    background: radial-gradient(ellipse at 45% 30%, #f2dcc9 0%, #e9cf9e 28%, #c9c0b4 48%, #2a2a2a 70%, #1c1c1c 100%);
    border-radius: 160px 160px 0 0;
    opacity: 0.9;
  }
  .arrow { position: absolute; top: 308px; }
  .arrow-prev { left: 36px; }
  .arrow-next { left: 1138px; }

  .footer-band { position: absolute; left: 0; top: 612px; width: 1200px; height: 63px; background: var(--band); color: var(--white); }
  .band-item { position: absolute; top: 17px; display: flex; align-items: center; gap: 14px; font-size: 12px; line-height: 14px; }
  .band-region { left: 174px; }
  .band-locations { left: 358px; }
  .legal { position: absolute; right: 173px; top: 20px; text-align: right; font-size: 10px; line-height: 14px; }
  .promo-pill {
    position: absolute; left: 534px; top: 592px; width: 235px; height: 39px;
    border-radius: 20px; background: var(--white); border: 2px solid var(--sky);
    color: var(--sky-deep); font-size: 10.5px; display: flex; align-items: center; justify-content: center;
  }
</style>
</head>
<body>
  <header>
    <div class="brand"><span class="brand-dot"></span><span class="brand-name">VornaDerm</span></div>
    <div class="brand-tagline">The experts in permanent hair removal</div>

    <div class="enquire">
      <svg width="15" height="15" viewBox="0 0 15 15"><circle cx="7.5" cy="7.5" r="7.5" fill="#aaaaaa"/><text x="7.5" y="11.5" font-size="11" text-anchor="middle" fill="#fff" font-family="serif">?</text></svg>
      <span>Have a question? <b>Enquire online</b></span>
    </div>
    <div class="social"><span></span><span></span><span></span></div>
    <a class="book-btn">Book your appointment</a>

    <nav class="main-nav">
      <a>Studios</a><a>Prices</a><a>About</a><a>VornaDerm</a><a>Jobs &amp; Careers</a><a>Franchise</a>
    </nav>
  </header>

  <main>
    <h1 class="headline">Come to us<br>and feel like<br>a princess</h1>
    <div class="why"><span class="why-dot"></span>Why Permanent Epilation?</div>
    <div class="why-links">The Method <span>/</span> Good to Know <span>/</span> Zones</div>

    <div class="hero-photo" role="img" aria-label="Photo of a smiling blonde woman in a black leather jacket, white shirt and black tie"></div>

    <svg class="arrow arrow-prev" width="24" height="32" viewBox="0 0 24 32"><polyline points="16,4 6,16 16,28" fill="none" stroke="#555" stroke-width="1.6"/></svg>
    <svg class="arrow arrow-next" width="24" height="32" viewBox="0 0 24 32"><polyline points="8,4 18,16 8,28" fill="none" stroke="#555" stroke-width="1.6"/></svg>
  </main>

  <footer class="footer-band">
    <div class="band-item band-region">
      <svg width="48" height="28" viewBox="0 0 48 28"><circle cx="24" cy="14" r="12" fill="none" stroke="#fff" stroke-width="2"/><ellipse cx="24" cy="14" rx="5" ry="12" fill="none" stroke="#fff" stroke-width="1.5"/><line x1="12" y1="14" x2="36" y2="14" stroke="#fff" stroke-width="1.5"/></svg>
      <span>Choose<br>your region</span>
    </div>
    <div class="band-item band-locations">
      <svg width="40" height="32" viewBox="0 0 40 32"><path d="M20 2a7 7 0 0 1 7 7c0 5-7 12-7 12s-7-7-7-12a7 7 0 0 1 7-7z" fill="none" stroke="#fff" stroke-width="2.2"/><circle cx="20" cy="9" r="2.5" fill="#fff"/><polyline points="12,20 6,30 34,30 28,20" fill="none" stroke="#fff" stroke-width="2.2"/></svg>
      <span>New available<br>locations</span>
    </div>
    <div class="legal">Terms &amp; Conditions &nbsp;|&nbsp; Privacy Policy<br>Copyright © 2015 VornaDerm. All Right Reserved</div>
  </footer>
  <a class="promo-pill">Sign up for our latest promotions</a>
</body>
</html>
```